Harrow Glen Whiskey Label

We are looking for a label to be made for our single batch whiskey. in the attached pdf you will see the lay out of the design. We are going to use a whiskey bottle with a cork. Some of the label you will need to leave some space for hand writing.

Target Market(s)

people who like craft beer and whiskey

Industry/Entity Type

Craft Distillery

Font styles to use
Decorative

Colors

Designer to choose colors to be used in the design.

Requirements
Must have
• room for hand writing informatiom

```html
<!DOCTYPE html>
<html lang="en">
<head>
<meta charset="utf-8">
<title>Harrow Glen Whiskey Label</title>
<link rel="stylesheet" href="https://fonts.googleapis.com/css2?family=Alegreya+SC:wght@400;500;700&family=Bebas+Neue&display=swap">
<style>
  :root {
    --backdrop: #6a6a6a;
    --label-black: #151515;
    --label-black-soft: #1d1d1d;
    --paper: #f4f4f2;
    --ink: #1a1a1a;
    --cream: #f1ece4;
    --copper-dark: #8a4a2c;
    --copper: #c27a5a;
    --copper-light: #e3a487;
  }
  * { box-sizing: border-box; margin: 0; padding: 0; }
  html, body { width: 1064px; height: 1200px; overflow: hidden; }
  body { background: var(--backdrop); position: relative; font-family: "Alegreya SC", Georgia, serif; }

  .label {
    position: absolute; left: 172px; top: 61px; width: 720px; height: 1078px;
    background: linear-gradient(180deg, var(--label-black-soft), var(--label-black) 60%, #111);
    box-shadow: 0 18px 40px rgba(0,0,0,.35);
    color: var(--cream);
    overflow: hidden;
  }
  .distillery-name {
    position: absolute; top: 74px; width: 100%; text-align: center;
    font-size: 18px; font-weight: 500; letter-spacing: 7px;
  }
  .product-name {
    position: absolute; top: 138px; width: 100%; text-align: center;
    font-family: "Bebas Neue", Impact, sans-serif; font-size: 96px; line-height: 1;
    letter-spacing: 3px;
    background: linear-gradient(180deg, var(--copper-light), var(--copper) 45%, var(--copper-dark));
    -webkit-background-clip: text; background-clip: text; color: transparent;
    filter: drop-shadow(0 2px 2px rgba(0,0,0,.6));
  }
  .product-type {
    position: absolute; top: 236px; width: 100%; text-align: center;
    font-size: 17px; letter-spacing: 1.4px;
  }

  .batch-card {
    position: absolute; left: 51px; top: 305px; width: 617px; height: 538px;
    color: var(--ink);
  }
  .batch-card svg { position: absolute; inset: 0; }
  .field { position: absolute; font-size: 17px; font-weight: 500; letter-spacing: .3px; }
  .field-source { left: 22px; top: 58px; }
  .field-aged { left: 22px; top: 166px; }
  .field-abv { left: 358px; top: 166px; }
  .field-bottle { left: 22px; top: 345px; }
  .field-of { left: 358px; top: 345px; }
  .rule-h { position: absolute; left: 26px; width: 564px; border-top: 2px dotted var(--ink); }
  .rule-v { position: absolute; left: 277px; border-left: 2px dotted var(--ink); }

  .producer {
    position: absolute; top: 880px; width: 100%; text-align: center;
    font-size: 18px; line-height: 22px; letter-spacing: 4px;
  }
  .volume {
    position: absolute; top: 966px; width: 100%; text-align: center;
    font-family: "Bebas Neue", Impact, sans-serif; font-size: 42px; line-height: 1;
    color: var(--copper);
  }
  .band-thin, .band-wide {
    position: absolute; left: 0; width: 100%;
    background: linear-gradient(90deg, var(--copper), var(--copper-light) 40%, var(--copper) 70%, var(--copper-dark));
  }
  .band-thin { top: 1014px; height: 8px; }
  .band-wide { top: 1032px; height: 46px; }
</style>
</head>
<body>
  <div class="label">
    <div class="distillery-name">IRON SPUR DISTILLERY</div>
    <h1 class="product-name">HARROW GLEN</h1>
    <div class="product-type">SPIRIT DISTILLED FROM MALT MASH AND HOPS</div>

    <div class="batch-card">
      <svg width="617" height="538" viewBox="0 0 617 538" aria-hidden="true">
        <defs>
          <pattern id="scallop-top" width="26" height="12" patternUnits="userSpaceOnUse" x="0" y="0">
            <circle cx="13" cy="0" r="10.5" fill="#151515"/>
          </pattern>
          <pattern id="scallop-bottom" width="26" height="12" patternUnits="userSpaceOnUse" x="0" y="526">
            <circle cx="13" cy="12" r="10.5" fill="#151515"/>
          </pattern>
        </defs>
        <rect width="617" height="538" fill="#f4f4f2"/>
        <rect width="617" height="12" fill="url(#scallop-top)"/>
        <rect y="526" width="617" height="12" fill="url(#scallop-bottom)"/>
      </svg>
      <div class="field field-source">DISTILLATE SOURCE:</div>
      <div class="rule-h" style="top:128px"></div>
      <div class="field field-aged">AGED:</div>
      <div class="field field-abv">% ALC. BY VOL.</div>
      <div class="rule-v" style="top:157px;height:138px"></div>
      <div class="rule-h" style="top:314px"></div>
      <div class="field field-bottle">BOTTLE:</div>
      <div class="field field-of">OF:</div>
      <div class="rule-v" style="top:335px;height:139px"></div>
    </div>

    <div class="producer">
      DISTILLED AND BOTTLE BY<br>
      IRON SPUR DISTILLERY LLC<br>
      14. ALDER ROW. &nbsp;FENWICK PA 17021
    </div>
    <div class="volume">750ML</div>
    <div class="band-thin"></div>
    <div class="band-wide"></div>
  </div>
</body>
</html>
```